Healer at the Hearth needs business card

We need a business card that reflects the look and feel of the new website at www.healerathehearth.ca

Our patient navigation and advocacy services are most commonly used by seniors who feel overwhelmed by the health care system and want someone on their side to advocate for their care. Individuals with ill parents or other family members may also come to rely on Healer at the Hearth to help them support their loved one through their health care journey. Ultimately, anyone who finds their health care experience challenging and wants someone completely focused on their needs can benefit from the services of our doctor / nurse team.

Business

Must have
• One design tailored for two clinician which should include: logo, name, title, tel, email, web address and tagline
Nice to have
• A banner image to create a similar look to the website at www.healerathehearth.ca
Should not have
• Too cluttered or busy - must be clean and professional

```html
<!DOCTYPE html>
<html lang="en">
<head>
<meta charset="utf-8">
<title>Healer at the Hearth – Business Card</title>
<link href="https://fonts.googleapis.com/css2?family=Open+Sans:wght@400;600;700&display=swap" rel="stylesheet">
<style>
  :root {
    --brand-red: #a51d24;
    --brand-blue: #1f5c8a;
    --ink: #222222;
    --paper: #ffffff;
    --backdrop: #9a9a9a;
    --photo-light: #eef1f3;
    --photo-mid: #d9dee2;
  }
  * { box-sizing: border-box; margin: 0; padding: 0; }
  html, body {
    width: 1200px; height: 900px; overflow: hidden;
    background: var(--backdrop);
    font-family: "Open Sans", Arial, sans-serif;
  }
  .stage {
    width: 1200px; height: 900px;
    display: flex; align-items: center; justify-content: center; gap: 40px;
  }
  .card {
    position: relative;
    width: 540px; height: 309px;
    border-radius: 16px;
    overflow: hidden;
    box-shadow: 0 10px 28px rgba(0,0,0,.25);
  }

  /* Front */
  .card--front { background: var(--brand-red); }
  .front-photo {
    position: absolute; right: 28px; top: 26px;
    width: 230px; height: 200px; border-radius: 22px;
    background: linear-gradient(135deg, var(--photo-light) 0%, var(--photo-mid) 60%, #e9d2c0 100%);
    border: 6px solid var(--paper);
  }
  .front-brand {
    position: absolute; left: 30px; bottom: 34px;
    display: flex; align-items: center; gap: 14px;
  }
  .brand-dot {
    width: 58px; height: 58px; border-radius: 50%;
    background: var(--paper);
  }
  .front-brand .brand-name {
    color: var(--paper); font-weight: 400; font-size: 31px; line-height: 1.05;
  }

  /* Back */
  .card--back { background: var(--paper); }
  .back-brand {
    position: absolute; left: 28px; top: 20px;
    display: flex; align-items: center; gap: 10px;
  }
  .back-brand .brand-dot { width: 42px; height: 42px; background: var(--brand-red); }
  .back-brand .brand-name {
    color: var(--brand-blue); font-weight: 400; font-size: 21px; line-height: 1.05;
  }
  .banner {
    position: absolute; left: 0; right: 0; top: 98px; height: 112px;
    background: linear-gradient(90deg, #f3f4f5 0%, var(--photo-light) 45%, #e6c9c9 62%, var(--photo-light) 78%, #e3e6e8 100%);
  }
  .person {
    position: absolute; left: 28px; top: 224px;
    color: var(--brand-red);
  }
  .person-name { font-weight: 700; font-size: 17px; letter-spacing: .3px; }
  .person-title { font-size: 11px; margin-top: 1px; }
  .contacts {
    position: absolute; right: 26px; top: 222px;
    list-style: none; font-size: 12px; color: var(--ink);
  }
  .contacts li { display: flex; align-items: center; gap: 8px; height: 17px; }
  .contacts svg { width: 12px; height: 12px; flex: none; }
</style>
</head>
<body>
<main class="stage">

  <section class="card card--front">
    <div class="front-photo" role="img" aria-label="Photo of a caregiver holding a patient's hand"></div>
    <div class="front-brand">
      <span class="brand-dot"></span>
      <span class="brand-name">Healer at<br>the Hearth</span>
    </div>
  </section>

  <section class="card card--back">
    <div class="back-brand">
      <span class="brand-dot"></span>
      <span class="brand-name">Healer at<br>the Hearth</span>
    </div>
    <div class="banner" role="img" aria-label="Photo of a doctor in a white coat holding a red heart, stethoscope around the neck"></div>
    <div class="person">
      <p class="person-name">JANE ROWAN</p>
      <p class="person-title">Director</p>
    </div>
    <ul class="contacts">
      <li>
        <svg viewBox="0 0 12 12"><circle cx="6" cy="6" r="6" fill="#a51d24"/><path d="M4 3.2l1 1.3-.6.7c.4.9 1 1.5 1.9 1.9l.7-.6 1.3 1-.6 1.1C5.6 8.4 3.6 6.4 3.4 3.8z" fill="#fff"/></svg>
        555 013 4872
      </li>
      <li>
        <svg viewBox="0 0 12 12"><circle cx="6" cy="6" r="6" fill="#a51d24"/><rect x="4.2" y="2.6" width="3.6" height="6.8" rx=".6" fill="#fff"/><rect x="4.8" y="3.4" width="2.4" height="4.4" fill="#a51d24"/></svg>
        555 019 2263
      </li>
      <li>
        <svg viewBox="0 0 12 12"><circle cx="6" cy="6" r="6" fill="#a51d24"/><rect x="3" y="4" width="6" height="4.2" fill="#fff"/><path d="M3 4l3 2.3L9 4" stroke="#a51d24" stroke-width=".7" fill="none"/></svg>
        jrowan@healerathehearth.ca
      </li>
      <li>
        <svg viewBox="0 0 12 12"><circle cx="6" cy="6" r="6" fill="#a51d24"/><circle cx="6" cy="6" r="3.4" fill="none" stroke="#fff" stroke-width=".7"/><ellipse cx="6" cy="6" rx="1.4" ry="3.4" fill="none" stroke="#fff" stroke-width=".7"/><path d="M2.6 6h6.8" stroke="#fff" stroke-width=".7"/></svg>
        www.healerathehearth.ca
      </li>
    </ul>
  </section>

</main>
</body>
</html>
```